Trifold - Harbor Lantern Therapy

Maren Holloway, Psy.D.Licensed Psychologist

this is for hypnosis and meditation
I like decorative font for my name (conservative decorative)

calming effect is most imortant

Target Market(s)

clients with depression, pain, anxiety - adults and aged

Industry/Entity Type

Conservative

Font styles to use
Serif

Colors
abd037
85cae6
cadf82
34a7d7
ffffff
886aae
6b449b

Requirements
Must have
• I like zen-like calming effects. lime Green, light blues and purple. I like waves and color.
• I like water and light, flowers and plants - bamboo, stacking rocks, ocean, water, lotus flowers
Should not have
• not too much purple
• Mostly green and blue

```html
<!DOCTYPE html>
<html lang="en">
<head>
<meta charset="utf-8">
<title>Harbor Lantern Therapy – Trifold</title>
<link rel="stylesheet" href="https://fonts.googleapis.com/css2?family=Poppins:wght@300;400;600;700&family=Passion+One:wght@700&family=Bitter:wght@500;700&display=swap">
<style>
  :root{
    --lime:#abd037;
    --lime-soft:#cadf82;
    --sky:#85cae6;
    --ocean:#34a7d7;
    --deep:#1c5f95;
    --navy:#1d4f86;
    --violet:#886aae;
    --plum:#6b449b;
    --ink:#555b61;
    --white:#ffffff;
    --stage:#eceeee;
  }
  *{box-sizing:border-box;margin:0;padding:0}
  html,body{width:757px;height:1200px;overflow:hidden;background:var(--stage)}
  body{font-family:"Poppins",sans-serif;position:relative}
  .trifold{position:absolute;left:0;top:306px;width:757px;height:588px;display:flex;box-shadow:0 6px 14px rgba(0,0,0,.25)}
  .panel{position:relative;height:100%;overflow:hidden}
  .panel--services{width:254px;background:var(--white)}
  .panel--contact{width:251px;background:linear-gradient(#fff 0,#f1f2f2 160px)}
  .panel--cover{width:252px;background:var(--ocean)}
  .panel svg.waves{position:absolute;left:0;top:0}

  /* services */
  .services-title{position:absolute;left:16px;top:14px;line-height:1.05}
  .services-title .lead{display:block;font-weight:700;font-size:19px;color:var(--lime)}
  .services-title .sub{display:block;font-weight:300;font-size:18px;color:var(--lime)}
  .services-rule{position:absolute;left:16px;top:62px;width:196px;height:1px;background:var(--lime-soft)}
  .services-list{position:absolute;left:0;top:74px;width:236px}
  .service{margin-bottom:9px}
  .service h3{display:inline-block;background:var(--lime);color:var(--white);font-size:8.4px;font-weight:600;line-height:1.15;padding:2px 8px 2px 17px}
  .service p{font-size:8px;line-height:1.36;color:var(--ink);padding:4px 0 0 17px;text-align:justify}
  .fee{position:absolute;left:17px;bottom:8px;width:225px;font-size:8.4px;line-height:1.3;color:var(--white)}

  /* contact */
  .contact-block{position:absolute;left:0;top:52px;width:100%;text-align:center;color:var(--navy)}
  .contact-name{font-size:11px;line-height:1.3}
  .contact-role{font-size:11px;font-weight:600;line-height:1.3}
  .motto{margin-top:7px;font-size:8.4px;line-height:1.4;color:var(--ocean)}
  .icon{display:block;margin:6px auto 1px}
  .office-label{font-size:10.5px;line-height:1.25}
  .office-address{font-size:8.4px;line-height:1.35;color:var(--ink)}
  .contact-phone{font-size:20px;font-weight:700;color:var(--navy);letter-spacing:.3px;margin-top:-2px}
  .sea-photo{position:absolute;left:0;top:160px;width:100%;height:330px;background:linear-gradient(180deg,rgba(133,202,230,0) 0,rgba(133,202,230,.55) 60px,#5fb7d9 150px,#2f8fbe 330px)}
  .center-name{position:absolute;left:0;top:300px;width:100%;text-align:center;color:var(--plum)}
  .center-name .word{font-size:17px;font-weight:600;letter-spacing:5px}
  .center-name .tag{font-size:8.4px;font-weight:600;letter-spacing:1.6px;margin-top:-2px}
  .center-mark{display:block;width:40px;height:40px;border-radius:50%;background:var(--violet);margin:0 auto 8px}
  .beach-photo{position:absolute;left:93px;top:430px;width:132px;height:132px;border-radius:50%;border:4px solid var(--white);background:linear-gradient(180deg,#bfe6f7 0,#5cc4e0 38%,#2ea6c9 58%,#e6cf95 72%,#d8b26c 100%)}
  .url-pill{position:absolute;left:50%;bottom:9px;transform:translateX(-50%);background:var(--lime);color:var(--navy);font-size:10px;padding:1px 14px;border-radius:9px;white-space:nowrap}

  /* cover */
  .lotus-photo{position:absolute;left:0;top:0;width:100%;height:370px;background:radial-gradient(circle at 62% 28%,#e7b62d 0,#c98b2a 9%,#9d82c8 21%,#886aae 42%,#4b2f6e 72%,#1d1424 100%)}
  .headline{position:absolute;left:0;top:216px;width:100%;text-align:center;color:var(--white);line-height:1}
  .headline .big{font-family:"Passion One",sans-serif;font-weight:700;font-size:44px;letter-spacing:.3px}
  .headline .light{font-size:23px;font-weight:300;margin-top:2px}
  .headline .bold{font-size:22px;font-weight:700;margin-top:1px}
  .cover-id{position:absolute;left:14px;top:414px;width:224px;height:46px;border-left:1px solid rgba(255,255,255,.85);border-right:1px solid rgba(255,255,255,.85);color:var(--white);text-align:center}
  .rule-row{position:absolute;left:-1px;right:-1px;display:flex;align-items:center;gap:6px;white-space:nowrap}
  .rule-row::before,.rule-row::after{content:"";flex:1;height:1px;background:rgba(255,255,255,.85)}
  .cover-name{top:-9px;height:18px;font-family:"Bitter",serif;font-weight:700;font-size:13.5px;line-height:18px}
  .cover-motto{font-family:"Bitter",serif;font-weight:700;font-size:19px;line-height:24px;padding-top:10px}
  .cover-role{bottom:-8px;height:16px;font-size:13px;font-weight:300;line-height:16px}
  .cover-focus{position:absolute;left:0;top:480px;width:100%;text-align:center;color:var(--white);font-size:13px;line-height:1.3}
  .cover-focus .light{font-weight:300}
  .cover-focus strong{font-weight:700}
  .cover-phone{font-size:19px;font-weight:400;margin-top:2px}
</style>
</head>
<body>
<main class="trifold">

  <section class="panel panel--services">
    <svg class="waves" width="254" height="588" viewBox="0 0 254 588" aria-hidden="true">
      <path d="M0 470 C80 515 170 520 254 488 L254 588 L0 588Z" fill="#abd037"/>
      <path d="M0 488 C80 535 170 540 254 505 L254 588 L0 588Z" fill="#ffffff"/>
      <path d="M0 510 C90 540 180 540 254 522 L254 588 L0 588Z" fill="#cadf82"/>
      <path d="M0 530 C90 550 180 548 254 535 L254 588 L0 588Z" fill="#1c5f95"/>
    </svg>
    <h1 class="services-title"><span class="lead">Psychological</span><span class="sub">Services</span></h1>
    <div class="services-rule"></div>

    <div class="services-list">
      <div class="service">
        <h3>Initial evaluation</h3>
        <p>Mental health assessment, diagnosis and comprehensive wellness planning.</p>
      </div>
      <div class="service">
        <h3>Harbor Lantern Therapy (HLT)</h3>
        <p>Resolve emotional distress, heartbreak and grief. HLT clears trauma at the subconscious level with hypnotic communication. The most troubling of memories are worked through and clients gain a sense of clarity, peace and power. Only a couple of sessions are needed to experience dramatic and long-lasting effects.</p>
      </div>
      <div class="service">
        <h3>Eye Movement Desensitization and<br>Reprocessing (EMDR)</h3>
        <p>Evidence-based treatment for post-traumatic stress disorder, anxiety, depression and adverse experiences. Experience relief and empowerment. More information at calmpath.org.</p>
      </div>
      <div class="service">
        <h3>Short-term talk therapy</h3>
        <p>Psychotherapy to create a more satisfying life. Proactive approach to seeking effective solutions for your most pressing emotional and relational problems.</p>
      </div>
      <div class="service">
        <h3>Meditation for Wellness</h3>
        <p>Personalized meditation for calm, healing and well-being.</p>
      </div>
    </div>

    <p class="fee">Fee Information: ElderShield and HarborGuard accepted and filed.</p>
  </section>

  <section class="panel panel--contact">
    <div class="sea-photo" role="img" aria-label="Photo of calm turquoise ocean water"></div>
    <svg class="waves" width="251" height="588" viewBox="0 0 251 588" aria-hidden="true">
      <path d="M0 520 C80 500 170 470 251 440 L251 588 L0 588Z" fill="#ffffff"/>
      <path d="M0 530 C90 512 170 485 251 456 L251 588 L0 588Z" fill="#abd037"/>
      <path d="M0 545 C90 528 170 505 251 480 L251 588 L0 588Z" fill="#34a7d7"/>
      <path d="M0 560 C90 548 170 530 251 510 L251 588 L0 588Z" fill="#1c5f95" opacity=".55"/>
    </svg>

    <div class="contact-block">
      <p class="contact-name">Maren Holloway, Psy.D.</p>
      <p class="contact-role">Licensed Psychologist</p>
      <p class="motto">· Heal the Past<br>·Embrace the Present<br>·Create the Future</p>
      <svg class="icon" width="10" height="13" viewBox="0 0 10 13" aria-hidden="true"><path d="M5 0C2.2 0 0 2.2 0 5c0 3.6 5 8 5 8s5-4.4 5-8c0-2.8-2.2-5-5-5zm0 7a2 2 0 1 1 0-4 2 2 0 0 1 0 4z" fill="#abd037"/></svg>
      <p class="office-label">Office Location:</p>
      <p class="office-address">Seaside Court<br>2210 Shore Rd #14<br>Harbor Cove, FL&nbsp;&nbsp;&nbsp;32900</p>
      <svg class="icon" width="16" height="11" viewBox="0 0 16 11" aria-hidden="true"><path d="M1 4C1 1 5 0 8 0s7 1 7 4l-3 1-1-2H5L4 5zM4 6h8l2 5H2z" fill="#abd037"/></svg>
      <p class="contact-phone">321 555-0147</p>
    </div>

    <div class="center-name">
      <span class="center-mark"></span>
      <p class="word">TIDEWELL</p>
      <p class="tag">wellness center</p>
    </div>

    <div class="beach-photo" role="img" aria-label="Round photo of a sandy beach and turquoise sea under a blue sky"></div>
    <p class="url-pill">www.tidewellhwc.com</p>
  </section>

  <section class="panel panel--cover">
    <div class="lotus-photo" role="img" aria-label="Close-up photo of a purple lotus flower with a golden centre"></div>
    <svg class="waves" width="252" height="588" viewBox="0 0 252 588" aria-hidden="true">
      <defs>
        <linearGradient id="cover-sea" x1="0" y1="0" x2="0" y2="1">
          <stop offset="0" stop-color="#34a7d7"/><stop offset="1" stop-color="#1c6fa8"/>
        </linearGradient>
      </defs>
      <path d="M0 372 C70 350 170 345 252 330 L252 588 L0 588Z" fill="#abd037"/>
      <path d="M0 385 C80 360 170 360 252 352 L252 588 L0 588Z" fill="#ffffff"/>
      <path d="M0 395 C80 372 170 372 252 366 L252 588 L0 588Z" fill="url(#cover-sea)"/>
    </svg>

    <h2 class="headline">
      <div class="big">Unleashing</div>
      <div class="light">the Power of the</div>
      <div class="bold">Mind for Healing</div>
      <div class="light">and Well-being</div>
    </h2>

    <div class="cover-id">
      <p class="rule-row cover-name">Maren Holloway, Psy.D.</p>
      <p class="cover-motto">Live Well, Love Well</p>
      <p class="rule-row cover-role">Licensed Psychologist</p>
    </div>

    <div class="cover-focus">
      <p><span class="light">Specializing in </span><strong>Adults</strong><span class="light"> and</span></p>
      <p><strong>Harbor Lantern Therapy</strong></p>
      <p class="cover-phone">321 555-0147</p>
    </div>

    <p class="url-pill">www.tidewellhwc.com</p>
  </section>

</main>
</body>
</html>
```